website re-design for: fern+lantern, complete vision care

we are a growing, cutting edge eye clinic with two locations in the palouse area of washington state, in the usa. we offer complete vision care, from spectacles and contacts to ocular disease management and treatment.

our current website was designed as a freebie, and was always meant to be a placeholder. we have reached a point where we would like our website to have a more stand-apart look and feel, while maintaining an intuitive user experience.

Target Market(s)

because our two clinics serve vastly different demographics, the website will have to speak to both. one clinic is located in a college town (majority of patients are 18-50 years+), while the other serves an older adult population (majority of patients 30-75 yrs+).

Industry/Entity Type

Health And Wellness

Logo Text

fern+lantern (including a logo lock-up version w/ "complete vision care")

Coding

Coded - Design and coding required

Number of Pages Required

5+ page

Font styles to use
Sans Serif
Other font styles liked:
• Verdana, and complementary fonts

Colors
606060
ffffff
33b8a4
86cfc6

Requirements
Must have
• - Pertinent contact information w/ Google maps
• - Clinic phone numbers at top of each page
• - An appointment request form
• - Page for Blog
• - Integrate with overall brand look and feel (e.g. Verdana font (we are open to complementary fonts), all lower case, except for prose,
• - Mobile friendly design
• - Code to maximize Search Engine Optimization (SEO)
Nice to have
• a design that speaks to the true nature of our business as an eye clinic, but feels different than typical eye care websites
Should not have
• this probably goes without saying, but the website should not have any political slant or otherwise bias

```html
<!DOCTYPE html>
<html lang="en">
<head>
<meta charset="utf-8">
<title>fern+lantern · complete vision care</title>
<link rel="stylesheet" href="https://fonts.googleapis.com/css2?family=Roboto:wght@300;400;500;700&family=Cormorant+Garamond:wght@500;600&display=swap">
<style>
:root{
  --ink:#3d3d3d;
  --text:#606060;
  --muted:#8a8a8a;
  --line:#dcdcdc;
  --paper:#ffffff;
  --teal:#33b8a4;
  --teal-dark:#2a9a89;
  --teal-soft:#86cfc6;
  --dark:#2b2b2b;
  --darker:#1f1f1f;
  --footer:#ebebeb;
}
*{box-sizing:border-box;margin:0;padding:0}
html,body{width:1200px;height:2540px;overflow:hidden;background:var(--paper)}
body{font-family:"Roboto",Verdana,sans-serif;color:var(--text);position:relative}
.page{position:relative;width:1200px;height:2540px}

/* header */
.top-bar{height:80px;display:flex;align-items:center;padding:0 180px;justify-content:space-between}
.brand{display:flex;align-items:center;gap:14px}
.brand-box{width:44px;height:44px;background:var(--ink)}
.brand-name{font-size:22px;font-weight:500;color:var(--ink);line-height:1}
.brand-sub{font-size:13px;color:var(--muted);margin-top:4px}
.contact-top{display:flex;gap:40px;font-size:12px}
.contact-top .item{display:flex;gap:10px;align-items:flex-start}
.contact-top .lbl{color:var(--muted)}
.contact-top .val{color:var(--ink);font-weight:500}
.contact-top svg{flex:none}

.main-nav{height:32px;background:var(--teal);display:flex;padding:0 180px}
.main-nav a{color:#fff;font-size:12px;font-weight:500;text-decoration:none;padding:0 16px;line-height:32px;letter-spacing:.3px}
.main-nav a.active{background:var(--teal-dark)}

/* hero */
.hero{position:relative;height:428px;background:linear-gradient(180deg,#c9b98a 0%,#b9a46a 30%,#7d8f3e 62%,#4f6f28 100%);text-align:center;color:#fff}
.hero-photo{position:absolute;inset:0}
.hero-inner{position:relative;padding-top:118px}
.hero h1{font-family:"Cormorant Garamond",Georgia,serif;font-weight:600;font-size:54px;letter-spacing:2px}
.hero .sub{font-size:19px;letter-spacing:2px;margin-top:4px;font-weight:300}
.hero .btn-ghost{display:inline-block;margin-top:34px;border:1px solid #fff;padding:11px 26px;font-size:13px;letter-spacing:1px}
.dots{position:absolute;bottom:22px;left:0;right:0;display:flex;justify-content:center;gap:8px}
.dots span{width:8px;height:8px;border-radius:50%;background:rgba(255,255,255,.55)}
.dots span.on{background:#fff}

/* welcome */
.welcome{text-align:center;padding:46px 260px 0}
.welcome h2{font-size:32px;font-weight:400;color:var(--ink);letter-spacing:.5px}
.divider{display:flex;align-items:center;justify-content:center;gap:12px;margin:14px 0 26px}
.divider i{display:block;width:150px;height:1px;background:var(--line)}
.welcome p{font-size:13px;line-height:1.9;color:var(--text)}

/* feature cards */
.features{display:flex;gap:28px;justify-content:center;margin-top:56px}
.card{width:310px;height:300px;border:1px solid var(--line);display:flex;position:relative;background:#fff}
.card .copy{width:150px;padding:26px 18px}
.card h3{font-size:17px;font-weight:500;color:var(--ink)}
.card p{font-size:10px;line-height:1.7;margin-top:10px;color:var(--muted)}
.card .btn{display:inline-block;margin-top:20px;border:1px solid var(--teal);color:var(--teal);font-size:10px;padding:6px 14px}
.card .photo{flex:1}

/* services */
.services{position:relative;margin-top:36px;height:450px;color:#fff}
.services svg.band{position:absolute;inset:0}
.services .content{position:relative;text-align:center;padding-top:78px}
.services h2{font-size:22px;font-weight:400;letter-spacing:2px}
.services .divider i{background:#666}
.svc-row{display:flex;justify-content:center;gap:40px;margin-top:6px}
.svc{width:240px}
.svc h3{font-size:16px;font-weight:500;margin-top:14px;line-height:1.35}
.svc p{font-size:10px;line-height:1.7;color:#bdbdbd;margin-top:12px}
.arrow{position:absolute;top:230px}

/* blogs */
.blogs{padding:34px 180px 0}
.blogs h2{font-size:22px;font-weight:400;color:var(--ink);letter-spacing:1px}
.blogs h2+i{display:block;width:60px;height:2px;background:var(--teal);margin:10px 0 22px}
.blog-row{display:flex;gap:36px}
.post{width:264px;border:1px solid var(--line)}
.post .photo{height:160px}
.post .body{padding:18px 14px 20px;display:flex;gap:10px;min-height:150px}
.post .ico{width:26px;height:26px;border-radius:50%;background:var(--teal);flex:none}
.post h4{font-size:14px;font-weight:500;color:var(--ink)}
.post p{font-size:10px;line-height:1.7;color:var(--muted);margin-top:8px}
.post .more{font-size:10px;color:var(--teal);margin-top:10px;font-weight:500}

/* footer */
.site-footer{position:absolute;left:0;right:0;top:2190px;height:350px;background:var(--footer)}
.foot-cols{display:flex;gap:60px;padding:46px 180px 0}
.foot-brand{width:200px}
.foot-brand .brand-box{width:40px;height:40px;margin-bottom:12px}
.social{display:flex;gap:6px;margin-top:16px}
.social span{width:18px;height:18px;border-radius:50%;border:1px solid var(--muted)}
.foot-col h5{font-size:12px;color:var(--ink);font-weight:700;margin-bottom:14px;letter-spacing:.5px}
.foot-col li{list-style:none;font-size:10px;line-height:1.9;color:var(--text)}
.foot-col .loc{font-size:10px;font-weight:700;color:var(--ink);margin-bottom:4px}
.loc-cols{display:flex;gap:70px}
.copyright{position:absolute;bottom:0;left:0;right:0;height:40px;border-top:1px solid var(--line);text-align:center;font-size:9px;line-height:40px;color:var(--muted)}
</style>
</head>
<body>
<div class="page">

<header>
  <div class="top-bar">
    <div class="brand">
      <div class="brand-box"></div>
      <div>
        <div class="brand-name">fern+lantern</div>
        <div class="brand-sub">complete vision care</div>
      </div>
    </div>
    <div class="contact-top">
      <div class="item">
        <svg width="18" height="18" viewBox="0 0 18 18"><rect x="1" y="4" width="16" height="11" fill="none" stroke="#606060" stroke-width="1.4"/><path d="M1 4l8 6 8-6" fill="none" stroke="#606060" stroke-width="1.4"/></svg>
        <div><div class="lbl">email address:</div><div class="val">hello@fernlantern.example</div></div>
      </div>
      <div class="item">
        <svg width="18" height="18" viewBox="0 0 18 18"><path d="M4 1h4l1 4-2 2c1 2 2 3 4 4l2-2 4 1v4c-8 1-14-5-13-13z" fill="#606060"/></svg>
        <div><div class="lbl">phone number:</div><div class="val">509-555-0142</div><div class="val">509-555-0187</div></div>
      </div>
    </div>
  </div>
  <nav class="main-nav">
    <a class="active">home</a><a>our eye doctor</a><a>our eye care clinic</a><a>eye care services</a><a>insurance</a><a>hours &amp; location</a>
  </nav>
</header>

<section class="hero">
  <div class="hero-photo" role="img" aria-label="Sunset over rolling green farmland hills"></div>
  <div class="hero-inner">
    <h1>an eye on the future</h1>
    <div class="sub">our new clinic in palouse</div>
    <span class="btn-ghost">request an appointment</span>
  </div>
  <div class="dots"><span class="on"></span><span></span><span></span><span></span></div>
</section>

<section class="welcome">
  <h2>welcome to fern+lantern</h2>
  <div class="divider"><i></i><svg width="26" height="14" viewBox="0 0 26 14"><path d="M1 7c6-8 18-8 24 0-6 8-18 8-24 0z" fill="none" stroke="#8a8a8a" stroke-width="1.3"/><circle cx="13" cy="7" r="3" fill="#8a8a8a"/></svg><i></i></div>
  <p>Eyes are important indicators of overall health, and comprehensive eye care goes beyond a prescription for glasses or contact lenses. At fern+lantern, we take the time to get to know you, your eye care history, and your vision needs. Our optometrists provide the expert care, advice, options, and follow up you need whether you are a new patient or an existing one.</p>
</section>

<section class="features">
  <article class="card">
    <div class="copy">
      <h3>our eye doctor</h3>
      <p>Our optometrist is a skilled specialist in understanding how the human eye really works, as well as diseases and conditions that affect your vision, many of which you may not notice.</p>
      <span class="btn">read more</span>
    </div>
    <div class="photo" role="img" aria-label="Portrait of the clinic's optometrist in a white coat" style="background:linear-gradient(160deg,#e4e4e4,#c9ccd0)"></div>
  </article>
  <article class="card">
    <div class="copy">
      <h3>our center</h3>
      <p>By staying current with the latest developments in eye care, prescription lenses and advances in contact lens technology, our clinic can provide you with the best vision.</p>
      <span class="btn">read more</span>
    </div>
    <div class="photo" role="img" aria-label="Close-up of a green eye" style="background:radial-gradient(circle at 50% 55%,#6f8e4a 0,#9ba98a 30%,#d9cfc4 60%,#efe9e3 100%)"></div>
  </article>
</section>

<section class="services">
  <svg class="band" width="1200" height="450" viewBox="0 0 1200 450" preserveAspectRatio="none">
    <path d="M0 60 Q600 -10 1200 60 V390 Q600 460 0 390Z" fill="var(--dark)"/>
    <path d="M0 60 Q600 -10 1200 60 V110 Q600 40 0 110Z" fill="var(--darker)"/>
    <path d="M0 398 Q600 468 1200 398 V450 H0Z" fill="#bdbdbd" opacity=".5"/>
  </svg>
  <svg class="arrow" style="left:200px" width="16" height="26" viewBox="0 0 16 26"><path d="M13 2L3 13l10 11" fill="none" stroke="#bbb" stroke-width="2"/></svg>
  <svg class="arrow" style="right:200px" width="16" height="26" viewBox="0 0 16 26"><path d="M3 2l10 11L3 24" fill="none" stroke="#bbb" stroke-width="2"/></svg>
  <div class="content">
    <h2>our services</h2>
    <div class="divider"><i></i><svg width="26" height="14" viewBox="0 0 26 14"><path d="M1 7c6-8 18-8 24 0-6 8-18 8-24 0z" fill="none" stroke="#ccc" stroke-width="1.3"/><circle cx="13" cy="7" r="3" fill="#ccc"/></svg><i></i></div>
    <div class="svc-row">
      <div class="svc">
        <svg width="40" height="40" viewBox="0 0 40 40"><circle cx="20" cy="20" r="18" fill="none" stroke="#fff" stroke-width="1.5"/><path d="M8 20c7-9 17-9 24 0-7 9-17 9-24 0z" fill="none" stroke="#fff" stroke-width="1.5"/><circle cx="20" cy="20" r="3.5" fill="#fff"/></svg>
        <h3>comprehensive<br>eye exams</h3>
        <p>Learn more about what problems can be spotted with an eye exam, what's involved in a comprehensive check and how to prepare for your visit.</p>
      </div>
      <div class="svc">
        <svg width="40" height="40" viewBox="0 0 40 40"><circle cx="20" cy="20" r="18" fill="none" stroke="#fff" stroke-width="1.5"/><circle cx="13" cy="21" r="5" fill="none" stroke="#fff" stroke-width="1.5"/><circle cx="27" cy="21" r="5" fill="none" stroke="#fff" stroke-width="1.5"/><path d="M18 20h4" stroke="#fff" stroke-width="1.5"/></svg>
        <h3>presbyopia diagnosis<br>and treatment</h3>
        <p>As we reach middle age, many of us notice that close work becomes harder. Find out why it happens and which lens options help most.</p>
      </div>
      <div class="svc">
        <svg width="40" height="40" viewBox="0 0 40 40"><circle cx="20" cy="20" r="18" fill="none" stroke="#fff" stroke-width="1.5"/><path d="M20 9c5 7 7 11 7 14a7 7 0 0 1-14 0c0-3 2-7 7-14z" fill="none" stroke="#fff" stroke-width="1.5"/></svg>
        <h3>dry eye disease<br>and treatment</h3>
        <p>Dry eye syndrome is a common condition that develops when your eyes do not produce enough tears. See the relief options we offer.</p>
      </div>
    </div>
  </div>
</section>

<section class="blogs">
  <h2>recent blogs</h2><i></i>
  <div class="blog-row">
    <article class="post">
      <div class="photo" role="img" aria-label="Patient during an eye examination" style="background:linear-gradient(135deg,#d7dde2,#9fb0bd)"></div>
      <div class="body"><span class="ico"></span><div><h4>your blog title here</h4><p>A short note on caring for your eyes through the seasons and simple habits that help.</p><div class="more">read more</div></div></div>
    </article>
    <article class="post">
      <div class="photo" role="img" aria-label="Optometrist examining a patient with a slit lamp" style="background:linear-gradient(135deg,#e6e2dc,#a7b7c4)"></div>
      <div class="body"><span class="ico"></span><div><h4>your blog title here</h4><p>What to expect at your first visit and how to get the most from your exam.</p><div class="more">read more</div></div></div>
    </article>
    <article class="post">
      <div class="photo" role="img" aria-label="Close-up of a contact lens on a fingertip" style="background:linear-gradient(135deg,#e9e9ea,#b9c6cf)"></div>
      <div class="body"><span class="ico"></span><div><h4>your blog title here</h4><p>Tips for choosing contact lenses that suit your daily routine and comfort.</p><div class="more">read more</div></div></div>
    </article>
  </div>
</section>

<footer class="site-footer">
  <div class="foot-cols">
    <div class="foot-brand">
      <div class="brand-box"></div>
      <div class="brand-name" style="font-size:18px">fern+lantern</div>
      <div class="brand-sub">complete vision care</div>
      <div class="social"><span></span><span></span><span></span><span></span></div>
    </div>
    <div class="foot-col">
      <h5>quick links</h5>
      <ul><li>our eye doctor</li><li>our eye care clinic</li><li>our services</li><li>contact</li></ul>
    </div>
    <div class="foot-col">
      <h5>contact us</h5>
      <div class="loc-cols">
        <ul><li class="loc">pullman location</li><li>120 Orchard Lane</li><li>Pullman, WA 99163</li><li>509-555-0142</li><li>hello@fernlantern.example</li></ul>
        <ul><li class="loc">clarkston location</li><li>48 River Bend Road</li><li>Clarkston, WA 99403</li><li>509-555-0187</li><li>hello@fernlantern.example</li></ul>
      </div>
    </div>
  </div>
  <div class="copyright">© 2024 fern+lantern. all rights reserved.</div>
</footer>

</div>
</body>
</html>
```